Medical Centre Website

We need a new design for a medical centre based in Perth, Western Australia called 'Tarvin Grove Medical Centre'.

The medical centre does general practitioner work including general checkups, ecg, heart checks, woman's health and more servicing children and adults. They also do home visits on occasions where the patient cannot attend the centre.

They would like an information/brochure website where visitors can read up on the practice, send email and view their location.

The client wish the design to be clean, fresh and light. The main colours are a light purple/blue and to a dark navy blue. The client would not want the logo to be altered in any way. This includes changing the words colours or the image.

The final design should represent a loving, family friendly practice where patients can come to receive the best treatments.

We just need the end product to be presented to un in a layed psd format. The fonts must be as per the W3C standards.

**IMPORTANT**
I have received heaps of chatlink invites in the past. To treat everyone fairly, I do not add people to my chatlink list as in the past people expected us to give them the prize. If you have questions, please ask them in pixel forum as it may benefit others who are also designing the site. If I need to, I will send a message to the user.
Updates

Hi Designers,

Most designs we have received have been overly cluttered. Are you able to simplify the designs.

Cheers, Dorian

Hi Designers,

Some of the designs are quite attractive but aremore cluttered than I would like. If you have a look at the following design, the design is very simple and straight to the point. A lot of designs have too much wording and the reader can be put off. We are looking something more like:

velmoxa.com.au

I would prefer to see designs and have opened up the contest for a further 7 days.

Designers,

We have received feedback from the client and Quite frankly he don’t really like any of them.They are too cluttered and Americanised. All drab blue colours.
 
If you have a look at template monster, these designs are better and cleaner. We do not want heaps of writing on the front page.

If you look at the eariler examples such as quorbeyclinic.com.au which I did myself, the client loves that simplicity of the site.

```html
<!DOCTYPE html>
<html lang="en">
<head>
<meta charset="utf-8">
<title>Tarvin Grove Medical Centre</title>
<link rel="stylesheet" href="https://fonts.googleapis.com/css2?family=Roboto:wght@400;500&family=Oswald:wght@400&display=swap">
<style>
:root{
  --navy:#0b4a8a;
  --navy-dark:#063d73;
  --nav-top:#1565b8;
  --nav-bottom:#0a4e98;
  --purple:#6a1bb5;
  --purple-light:#8a45cf;
  --purple-text:#6a2bc0;
  --text:#444;
  --muted:#555;
  --white:#fff;
}
*{box-sizing:border-box;margin:0;padding:0}
html,body{width:1127px;height:1200px;overflow:hidden;background:#fff}
body{font-family:'Roboto',sans-serif;color:var(--text)}
.page{position:relative;width:1127px;height:1200px;overflow:hidden}

.site-header{position:absolute;left:0;top:0;width:100%;height:118px;background:linear-gradient(#fff,#f1f1f1)}
.brand{position:absolute;left:122px;top:34px;display:flex;align-items:center;gap:12px}
.brand-mark{width:34px;height:34px;border-radius:50%;background:var(--navy)}
.brand-name{font-size:30px;font-weight:400;color:var(--navy);line-height:1.05}
.phone{position:absolute;right:122px;top:46px;display:flex;align-items:center;gap:10px;font-size:30px;color:var(--purple-text)}

.main-nav{position:absolute;left:0;top:118px;width:100%;height:48px;background:linear-gradient(var(--nav-top),var(--nav-bottom))}
.main-nav ul{list-style:none;display:flex;margin-left:122px;height:100%}
.main-nav li{display:flex;align-items:center;padding:0 23px;color:#fff;font-size:14.5px;letter-spacing:.3px;border-right:1px solid rgba(255,255,255,.18)}
.main-nav li:first-child{padding-left:20px}
.main-nav li:last-child{border-right:0}

.hero{position:absolute;left:0;top:166px;width:100%;height:421px}
.hero-photo{position:absolute;inset:0;background:linear-gradient(90deg,#c9d2dc 0%,#e6e2da 30%,#d8dde3 48%,#f1ede6 70%,#f6f3ee 100%)}
.hero-copy{position:absolute;right:122px;top:164px;text-align:right}
.hero-title{font-family:'Oswald',sans-serif;font-size:33px;color:var(--navy);font-weight:400;letter-spacing:-.2px}
.hero-sub{font-size:19px;color:#333;line-height:22px;margin-top:6px}
.btn{display:inline-block;background:var(--purple);color:#fff;text-transform:uppercase;border-radius:2px}
.hero .btn{margin-top:24px;font-size:16.5px;padding:7px 10px;letter-spacing:.3px}
.dots{position:absolute;right:122px;top:376px;display:flex;gap:6px}
.dots span{width:19px;height:19px;border-radius:50%;background:#6c9cc5}
.dots span:first-child{background:#0c5cb2}

.services{position:absolute;left:122px;top:611px;display:flex;gap:19px}
.service{width:207px;height:209px;background:linear-gradient(var(--purple-light),var(--purple));border:1px solid #5a129e;border-radius:2px;color:#fff;text-align:center;padding-top:12px}
.service-art{width:110px;height:90px;margin:0 auto;border-radius:8px;background:radial-gradient(circle,rgba(255,255,255,.35),rgba(255,255,255,.05))}
.service h3{font-weight:400;font-size:20px;margin-top:16px;letter-spacing:.3px}
.service p{font-size:13px;line-height:19px;margin-top:5px;padding:0 6px}

.welcome{position:absolute;left:122px;top:853px;width:650px}
.welcome h2{font-weight:400;font-size:23px;color:#333}
.welcome h2 span{color:var(--navy)}
.welcome-photo{position:absolute;left:0;top:47px;width:207px;height:181px;border:1px solid #ccc;background:linear-gradient(135deg,#e9eef4,#c8d4e2 45%,#e8d9c8 75%,#f3efe9)}
.welcome-text{position:absolute;left:227px;top:45px;width:420px;font-size:13px;line-height:21.6px;color:var(--muted)}
.welcome .btn{position:absolute;left:225px;top:193px;font-size:13px;padding:9px 12px}

.hours{position:absolute;left:798px;top:857px;width:207px;height:230px;background:linear-gradient(#f3f3f3,#ebebeb);border:1px solid #d6d6d6;border-radius:2px;text-align:center}
.hours h2{font-weight:400;font-size:25px;color:#333;text-align:left;padding:11px 0 0 14px}
.hours dl{margin-top:9px}
.hours dt{color:var(--purple-text);font-size:14.5px;margin-top:7px}
.hours dt:first-child{margin-top:0}
.hours dd{color:#333;font-size:15px}

.site-footer{position:absolute;left:0;top:1106px;width:100%;height:94px;background:var(--navy-dark);color:#fff}
.copyright{position:absolute;left:122px;top:30px;font-size:12px;line-height:19px;letter-spacing:.2px}
.social{position:absolute;right:122px;top:32px;display:flex;align-items:center;gap:5px;font-size:15px}
.social span{margin-right:3px}
.social i{display:block;width:28px;height:28px;border-radius:3px}
.social i.a{background:#3b5a9b}
.social i.b{background:#38a8dd}
.social i.c{background:#c4302b}
</style>
</head>
<body>
<div class="page">
  <header class="site-header">
    <div class="brand"><span class="brand-mark"></span><span class="brand-name">Tarvin Grove<br>Medical Centre</span></div>
    <div class="phone">
      <svg width="28" height="28" viewBox="0 0 24 24" aria-hidden="true"><path fill="#c0392b" d="M6.6 10.8a15.1 15.1 0 0 0 6.6 6.6l2.2-2.2c.3-.3.7-.4 1-.2 1.1.4 2.3.6 3.6.6.6 0 1 .4 1 1V20c0 .6-.4 1-1 1A17 17 0 0 1 3 4c0-.6.4-1 1-1h3.5c.6 0 1 .4 1 1 0 1.3.2 2.5.6 3.6.1.3 0 .7-.2 1z"/></svg>
      08 555 0192
    </div>
  </header>

  <nav class="main-nav">
    <ul>
      <li>Home</li><li>About Us</li><li>Services</li><li>Make a Appointment</li><li>Patient Care</li><li>Testimonials</li><li>Contact Us</li>
    </ul>
  </nav>

  <section class="hero">
    <div class="hero-photo" role="img" aria-label="Photo of a smiling doctor talking with an elderly patient"></div>
    <div class="hero-copy">
      <h1 class="hero-title">Tarvin Grove Medical Centre</h1>
      <p class="hero-sub">We have medical centre based in Perth,<br>Western Australia</p>
      <a class="btn">Get Appointment</a>
    </div>
    <div class="dots"><span></span><span></span><span></span><span></span></div>
  </section>

  <section class="services">
    <article class="service"><div class="service-art" role="img" aria-label="Illustration of a clipboard and stethoscope"></div><h3>General Checkups</h3><p>Euismod, dui purus auctor tellus, et interdum lacus lectus et ante...</p></article>
    <article class="service"><div class="service-art" role="img" aria-label="Illustration of an ECG monitor"></div><h3>ECG Test</h3><p>Euismod, dui purus auctor tellus, et interdum lacus lectus et ante...</p></article>
    <article class="service"><div class="service-art" role="img" aria-label="Illustration of a heart with a stethoscope"></div><h3>Heart Checkups</h3><p>Euismod, dui purus auctor tellus, et interdum lacus lectus et ante...</p></article>
    <article class="service"><div class="service-art" role="img" aria-label="Illustration of a woman beside a medical bag"></div><h3>Woman's Health</h3><p>Euismod, dui purus auctor tellus, et interdum lacus lectus et ante...</p></article>
  </section>

  <section class="welcome">
    <h2>Welcome to <span>Our Medical Centre</span></h2>
    <div class="welcome-photo" role="img" aria-label="Photo of a doctor with a family of three"></div>
    <p class="welcome-text">Aliquam molestie, mi et imperdiet euismod, dui purus auctor tellus, et interdum lacus lectus et ante. Sed accumsan sollicitudin sapien, sit amet adipiscing turpis gravida ac. In congue, neque ac lobortis volutpat, libero mauris varius mi, vitae suscipit ipsum ligula vitae risus. Duis aliquam nibh a dui iaculis viverra id a velit. Vivamus egestas risus in magna varius commodo.</p>
    <a class="btn">Read More</a>
  </section>

  <aside class="hours">
    <h2>Practice Hours</h2>
    <dl>
      <dt>Monday - Friday:</dt><dd>8:00am - 6:00pm</dd>
      <dt>Saturday:</dt><dd>9:00am - 12:00pm</dd>
      <dt>Sunday:</dt><dd>9:00am - 12:00pm</dd>
    </dl>
  </aside>

  <footer class="site-footer">
    <p class="copyright">Copyright © 2013. Tarvin Grove Medical Centre.<br>All Right Reserved</p>
    <div class="social"><span>Get in Touch:</span><i class="a"></i><i class="b"></i><i class="c"></i></div>
  </footer>
</div>
</body>
</html>
```